Stationery - business cards, headers/footers, powerpoint templates
2 sets of business cards. One for 'Owen Tasker' and one for 'Lars Pemberton'. No job titles needed
Stationery - business cards, headers/footers, powerpoint templates - Consulting
Creative Brief
Simple
1. Lars Pemberton 2. Owen Tasker
Grand Cayman Cayman Islands
Lars@coverloom.ky
coverloom.ky
2 sets of business cards required - one for Lars Pemberton and one for Owen TAsker. Note that our email addresses are Lars@coverloom.ky and Owen@coverloom.ky
Modern/clean logo

```html
<!DOCTYPE html>
<html lang="en">
<head>
<meta charset="UTF-8">
<title>Coverloom Business Cards</title>
<link href="https://fonts.googleapis.com/css2?family=Open+Sans:wght@400;600;700;800&display=swap" rel="stylesheet">
<style>
  :root {
    --pink: #f25cc9;
    --ink: #1e1e1e;
    --grey: #8f8f8f;
    --rule: #cfcfcf;
    --card: #ffffff;
    --backdrop: #e6e6e8;
  }
  * { margin: 0; padding: 0; box-sizing: border-box; }
  html, body { width: 1200px; height: 768px; overflow: hidden; }
  body {
    background: var(--backdrop);
    font-family: "Open Sans", Arial, sans-serif;
    display: flex;
    align-items: center;
    justify-content: center;
    gap: 40px;
  }
  .card {
    position: relative;
    width: 540px;
    height: 310px;
    background: var(--card);
    box-shadow: 0 6px 18px rgba(0,0,0,0.18);
    overflow: hidden;
  }
  .wordmark {
    position: absolute;
    display: flex;
    align-items: center;
    gap: 8px;
    font-weight: 800;
    color: var(--ink);
    letter-spacing: -1px;
    line-height: 1;
  }
  .wordmark-square {
    width: 14px;
    height: 14px;
    background: var(--pink);
  }
  /* back side */
  .card-back .wordmark { left: 150px; top: 112px; font-size: 46px; }
  .back-stripe {
    position: absolute; left: 0; right: 0; bottom: 36px;
    height: 3px; background: var(--rule);
  }
  .back-band {
    position: absolute; left: 0; right: 0; bottom: 0;
    height: 30px; background: var(--pink);
    display: flex; align-items: center; padding-left: 18px;
  }
  .back-band span { color: #fff; font-size: 8px; font-weight: 600; letter-spacing: 0.5px; }
  /* front side */
  .card-front .wordmark { left: 48px; top: 106px; font-size: 36px; }
  .divider {
    position: absolute; left: 290px; top: 74px;
    width: 1px; height: 110px; background: var(--rule);
  }
  .contact {
    position: absolute; left: 306px; top: 76px;
    color: var(--grey); font-size: 12px; line-height: 1.45;
  }
  .contact-name { color: var(--pink); font-weight: 700; font-size: 17px; margin-bottom: 4px; }
  .contact-line { display: flex; align-items: center; gap: 6px; }
  .contact-line svg { width: 10px; height: 10px; flex: none; }
  .contact-gap { margin-top: 6px; }
  .front-curve { position: absolute; left: 0; bottom: 0; width: 540px; height: 310px; }
</style>
</head>
<body>
  <div class="card card-back">
    <div class="wordmark"><span class="wordmark-square"></span>coverloom</div>
    <div class="back-stripe"></div>
    <div class="back-band"><span>coverloom.ky</span></div>
  </div>

  <div class="card card-front">
    <svg class="front-curve" viewBox="0 0 540 310" aria-hidden="true">
      <path d="M0 238 Q300 300 540 290 L540 310 L0 310 Z" fill="var(--pink)"/>
      <path d="M0 232 Q300 294 540 284" fill="none" stroke="var(--ink)" stroke-width="2"/>
    </svg>
    <div class="wordmark"><span class="wordmark-square"></span>coverloom</div>
    <div class="divider"></div>
    <div class="contact">
      <div class="contact-name">Lars Pemberton</div>
      <div>Grand Cayman</div>
      <div>Cayman Islands</div>
      <div class="contact-line contact-gap">
        <svg viewBox="0 0 10 10"><path d="M2 1 L4 1 L4.6 3.2 L3.5 4 Q4.6 6 6 6.5 L6.8 5.4 L9 6 L9 8 Q8.5 9 7.5 9 Q1 8 1 2 Q1 1 2 1 Z" fill="var(--pink)"/></svg>
        <span>+1(345) 555-0142</span>
      </div>
      <div class="contact-line">
        <svg viewBox="0 0 10 10"><rect x="0.5" y="2" width="9" height="6.5" rx="1" fill="var(--pink)"/><path d="M1 2.5 L5 5.6 L9 2.5" fill="none" stroke="#fff" stroke-width="0.9"/></svg>
        <span>Lars@coverloom.ky</span>
      </div>
      <div class="contact-line">
        <svg viewBox="0 0 10 10"><circle cx="5" cy="5" r="4.5" fill="var(--pink)"/><path d="M0.5 5 H9.5 M5 0.5 Q2.5 5 5 9.5 M5 0.5 Q7.5 5 5 9.5" fill="none" stroke="#fff" stroke-width="0.7"/></svg>
        <span>coverloom.ky</span>
      </div>
    </div>
  </div>
</body>
</html>
```